Business card design for Allied Healthcare provider

We would like a design for front and back of business cards. The design must resonate with all levels of customers from patients, to other health providers and medical. Must also resonate with corporate customers

Target Market(s)

patients, medical practitioners, other health providers and corporate.

Industry/Entity Type

healthcare

Contact Information for Business Card

name, logo, phone and fax numbers, email, website

Requirements
Must have
• not allowing me to change this, but the card must be double sided!! Please take note
Nice to have
• a fresh yet bold design to catch attention.

```html
<!DOCTYPE html>
<html lang="en">
<head>
<meta charset="utf-8">
<title>Vitalcrest business card</title>
<link href="https://fonts.googleapis.com/css2?family=Quicksand:wght@500;700&display=swap" rel="stylesheet">
<style>
  :root {
    --navy: #1b2d57;
    --indigo: #24195a;
    --gold: #fbb91f;
    --white: #ffffff;
    --backdrop: #d9dcdf;
  }
  html, body {
    margin: 0;
    width: 1200px;
    height: 1200px;
    overflow: hidden;
    background: var(--backdrop);
  }
  .canvas {
    position: relative;
    width: 1200px;
    height: 1200px;
  }
  .card {
    position: absolute;
    left: 201px;
    width: 797px;
    height: 456px;
    display: block;
  }
  .card--front { top: 122px; }
  .card--back { top: 625px; }
  .brand-name {
    font-family: "Quicksand", sans-serif;
    font-weight: 700;
    fill: var(--navy);
  }
  .contact-line {
    font-family: "Quicksand", sans-serif;
    font-weight: 500;
    font-size: 15px;
    fill: var(--white);
    letter-spacing: 0.3px;
  }
  .contact-line--phone {
    font-weight: 700;
    font-size: 17px;
  }
</style>
</head>
<body>
<main class="canvas">

  <!-- Front side -->
  <svg class="card card--front" viewBox="0 0 664 380" aria-label="Vitalcrest card front">
    <defs>
      <clipPath id="front-clip"><rect width="664" height="380"/></clipPath>
    </defs>
    <g clip-path="url(#front-clip)">
      <rect class="card-surface" width="664" height="380" fill="var(--navy)"/>
      <circle class="ring ring--gold" cx="407" cy="72" r="250" fill="none" stroke="var(--gold)" stroke-width="8"/>
      <circle class="panel-disc" cx="407" cy="72" r="232" fill="var(--white)" stroke="var(--indigo)" stroke-width="8"/>
      <text class="brand-name" x="402" y="135" font-size="44" text-anchor="middle">Vitalcrest</text>
    </g>
  </svg>

  <!-- Back side -->
  <svg class="card card--back" viewBox="0 0 664 380" aria-label="Vitalcrest card back">
    <defs>
      <clipPath id="back-clip"><rect width="664" height="380"/></clipPath>
    </defs>
    <g clip-path="url(#back-clip)">
      <rect class="card-surface" width="664" height="380" fill="var(--navy)"/>
      <circle class="ring ring--gold" cx="56" cy="190" r="250" fill="none" stroke="var(--gold)" stroke-width="8"/>
      <circle class="panel-disc" cx="56" cy="190" r="232" fill="var(--white)" stroke="var(--indigo)" stroke-width="8"/>
      <text class="brand-name" x="41" y="199" font-size="28">Vitalcrest</text>

      <g class="contact-list">
        <g class="contact-icon contact-icon--address" transform="translate(406 159)">
          <circle r="9" fill="var(--gold)"/>
          <path d="M0 5 C-4 0 -4 -1 -4 -2 A4 4 0 0 1 4 -2 C4 -1 4 0 0 5Z" fill="var(--navy)"/>
          <circle cy="-2" r="1.5" fill="var(--gold)"/>
        </g>
        <text class="contact-line" x="428" y="164">Address vitalcrest</text>

        <g class="contact-icon contact-icon--phone" transform="translate(406 191)">
          <circle r="9" fill="var(--gold)"/>
          <path d="M-4 -4 L-2 -5 L0 -2 L-1.5 -1 Q0 2 1.5 2.5 L2.5 1 L5 3 L4 5 Q-4 4 -4 -4Z" fill="var(--navy)"/>
        </g>
        <text class="contact-line contact-line--phone" x="428" y="197">0123456789</text>

        <g class="contact-icon contact-icon--email" transform="translate(406 220)">
          <circle r="9" fill="var(--gold)"/>
          <rect x="-5" y="-3.5" width="10" height="7" fill="var(--navy)"/>
          <path d="M-5 -3.5 L0 0.5 L5 -3.5" fill="none" stroke="var(--gold)" stroke-width="1"/>
        </g>
        <text class="contact-line" x="428" y="225">@vitalcrest.com</text>

        <g class="contact-icon contact-icon--web" transform="translate(406 246)">
          <circle r="9" fill="var(--gold)"/>
          <g fill="none" stroke="var(--navy)" stroke-width="1">
            <circle r="5"/>
            <ellipse rx="2.2" ry="5"/>
            <line x1="-5" y1="0" x2="5" y2="0"/>
          </g>
        </g>
        <text class="contact-line" x="428" y="251">www.vitalcrest.com</text>
      </g>
    </g>
  </svg>

</main>
</body>
</html>
```